Infographic about product packaging for aged care

We need an infographic that will be published in Larder Digest, to illustrate some points alongside our Aged Care feature.

Vector style preferred. Please incorporate bright blue and yellow into the colour scheme (Blue: 79C/28M/0Y/0K, Yellow: C5/M2/Y100/K0). Feel free to use other colours to supplement this palette.

Please use the image attached to this brief as a guide to colour and style. This is the opening page of the article.

Dimensions: 102mm x 102mm

Content:
- One in two Australians face difficulty opening or reading packaging
- 53 percent have suffered an injury as a result of inaccessible packaging.
- One in two people face at least one form of restriction:
o sensory (vision, hearing, taste)
o motion (strength, dexterity, locomotion, reach & stretch)
o cognitive (communication & understanding, intellectual functioning)

```html
<!DOCTYPE html>
<html lang="en">
<head>
<meta charset="utf-8">
<title>Packaging Accessibility – Larder Digest</title>
<link rel="stylesheet" href="https://fonts.googleapis.com/css2?family=Poppins:wght@500;600;700&display=swap">
<style>
  :root {
    --sky-centre: #b4e6f3;
    --sky-edge: #1c9bd8;
    --ink-blue: #0a70a6;
    --bright-yellow: #f6e800;
  }
  html, body {
    margin: 0;
    padding: 0;
    width: 1200px;
    height: 1200px;
    overflow: hidden;
  }
  .infographic {
    display: block;
    width: 1200px;
    height: 1200px;
    font-family: "Poppins", "Century Gothic", sans-serif;
  }
  .badge { fill: var(--bright-yellow); }
  .numeral { fill: var(--ink-blue); font-weight: 700; }
  .stat-text { fill: var(--ink-blue); font-weight: 600; }
  .accent-text { fill: var(--bright-yellow); font-weight: 600; }
  .illustration-area { fill: var(--bright-yellow); }
  .list-icon { fill: var(--bright-yellow); }
</style>
</head>
<body>
<svg class="infographic" viewBox="0 0 1200 1200" xmlns="http://www.w3.org/2000/svg" role="img" aria-label="Infographic on packaging accessibility for aged care">
  <defs>
    <radialGradient id="sky" cx="0.45" cy="0.5" r="0.75">
      <stop offset="0" stop-color="var(--sky-centre)"/>
      <stop offset="1" stop-color="var(--sky-edge)"/>
    </radialGradient>
  </defs>
  <rect class="background" width="1200" height="1200" fill="url(#sky)"/>

  <!-- Headline statistic: one in two -->
  <g class="stat-one-in-two">
    <circle class="badge" cx="265" cy="192" r="126"/>
    <circle class="badge" cx="432" cy="205" r="66"/>
    <circle class="badge" cx="580" cy="190" r="130"/>
    <text class="numeral" x="218" y="288" font-size="270">1</text>
    <text class="numeral" x="388" y="225" font-size="96">in</text>
    <text class="numeral" x="495" y="288" font-size="270">2</text>
  </g>
  <text class="stat-text" x="114" y="409" font-size="33">Australians face <tspan class="accent-text" font-size="64" font-weight="700">difficulty</tspan></text>
  <text class="stat-text" x="130" y="452" font-size="33">opening or reading packaging.</text>

  <!-- Illustration area -->
  <rect class="illustration-area" x="700" y="55" width="430" height="515" rx="120" role="img" aria-label="Illustration of a person with an arm in a sling"/>

  <!-- Injury statistic -->
  <g class="stat-injury">
    <circle class="badge" cx="245" cy="563" r="90"/>
    <circle class="badge" cx="360" cy="698" r="86"/>
    <text class="numeral" x="205" y="625" font-size="175">1</text>
    <text class="numeral" x="270" y="660" font-size="56">in</text>
    <text class="numeral" x="312" y="760" font-size="175">2</text>
    <text class="numeral" x="428" y="650" font-size="180">53</text>
    <text class="numeral" x="712" y="670" font-size="108" font-weight="600">percent</text>
  </g>
  <text class="stat-text" x="462" y="715" font-size="32">have suffered an injury as a result of</text>
  <text class="stat-text" x="555" y="757" font-size="32">inaccessible packaging.</text>

  <!-- Restriction list -->
  <text x="118" y="845" font-size="22">
    <tspan class="accent-text">people face at </tspan><tspan class="accent-text" font-size="38">least one</tspan><tspan class="stat-text"> form of </tspan><tspan class="stat-text" font-size="60" font-weight="700">restriction:</tspan>
  </text>

  <g class="restriction sensory">
    <rect class="list-icon" x="120" y="858" width="62" height="80" rx="30" role="img" aria-label="Ear icon"/>
    <text x="200" y="907" font-size="56"><tspan class="stat-text" font-weight="700">o sensory</tspan><tspan class="accent-text" font-size="32"> (vision, hearing, taste)</tspan></text>
  </g>

  <g class="restriction motion">
    <rect class="list-icon" x="116" y="948" width="72" height="82" rx="22" role="img" aria-label="Raised hand icon"/>
    <text x="200" y="980" font-size="56"><tspan class="stat-text" font-weight="700">o motion</tspan><tspan class="accent-text" font-size="32"> (strength, dexterity,</tspan></text>
    <text class="accent-text" x="200" y="1022" font-size="32">locomotion, reach &amp; stretch)</text>
  </g>

  <g class="restriction cognitive">
    <ellipse class="list-icon" cx="143" cy="1092" rx="44" ry="24" role="img" aria-label="Lips icon"/>
    <text x="203" y="1090" font-size="56"><tspan class="stat-text" font-weight="700">o cognitive</tspan><tspan class="accent-text" font-size="32"> (communication &amp;</tspan></text>
    <text class="accent-text" x="203" y="1132" font-size="32">understanding, intellectual functioning)</text>
  </g>
</svg>
</body>
</html>
```